professional looking data specialist website

I've recently had a new logo designed and I'm now looking to get a professional looking website built. This is for a new company that specialises in data. We look to support companies with business intelligence, report modelling, data governance to new european legislation (GDPR). We are offer consultancy or we can attend site and complete work when required. Our target arket is united kingdom wide and we are specifically aiming at small to medium sized companies.

Target Market(s)

small to medium enterprise companies from all industries

Industry/Entity Type

Professional Service

Coding

Coded - Design and coding required

Number of Pages Required

4 page

Font styles to use
Sans Serif

Colors

Designer to choose colors to be used in the design.

Requirements
Must have
• Professional look including the company logo, need to have ability to request more information from us so needs a inquiries page, seperate pages for the different offerings, data governance, report modelling, business intelligence implementation, data protection
Nice to have
• any website interaction, animation, etc
Should not have
• too many colours, too busy pages, must look professional

```html
<!DOCTYPE html>
<html lang="en">
<head>
<meta charset="utf-8">
<title>NorvaleData Ltd</title>
<link href="https://fonts.googleapis.com/css2?family=Jost:wght@300;400;500;700&family=Roboto+Condensed:wght@400;700&display=swap" rel="stylesheet">
<style>
:root{
  --blue:#0e6db7;
  --blue-deep:#0b5a9c;
  --blue-light:#1a80cc;
  --navy:#172230;
  --navy-2:#2a3646;
  --ink:#333b45;
  --grey:#6b7078;
  --line:#c9ced4;
  --white:#ffffff;
}
*{margin:0;padding:0;box-sizing:border-box}
html,body{width:1200px;height:2469px;overflow:hidden;background:var(--white)}
body{position:relative;font-family:"Jost",sans-serif;color:var(--ink)}
.abs{position:absolute}

/* nav */
.site-nav{position:absolute;top:0;left:0;width:1200px;height:79px;background:var(--white);z-index:5}
.nav-link{position:absolute;top:28px;font-size:18px;color:#444;transform:translateX(-50%)}
.nav-link.active{color:var(--blue)}
.nav-link.active::after{content:"";position:absolute;left:-14px;right:-14px;bottom:-10px;height:2px;background:var(--blue)}
.brand{position:absolute;top:22px;left:600px;transform:translateX(-50%);display:flex;align-items:center;gap:8px;font-size:22px;font-weight:500;color:var(--blue);white-space:nowrap}
.brand-mark{width:22px;height:22px;background:var(--blue)}

/* hero */
.hero{position:absolute;top:79px;left:0;width:1200px;height:576px;background:linear-gradient(120deg,#2b3848 0%,var(--navy) 45%,#101822 100%);clip-path:polygon(0 0,100% 0,100% 545px,695px 545px,665px 576px,535px 576px,505px 545px,0 545px)}
.hero-title{position:absolute;left:79px;top:160px;font-size:72px;font-weight:700;color:var(--white);letter-spacing:.5px}
.hero-sub{position:absolute;left:79px;top:255px;font-size:33px;font-weight:700;color:var(--white)}
.hero-text{position:absolute;left:79px;top:303px;width:600px;font-size:17.5px;line-height:22px;color:#e6e9ee;font-weight:300}
.btn-light{position:absolute;left:77px;top:382px;width:173px;height:49px;background:var(--white);color:#222;font-size:20px;display:flex;align-items:center;justify-content:center}
.slider-arrow{position:absolute;top:234px;width:52px;height:52px;border-radius:50%;background:rgba(0,0,0,.45);border:1px solid rgba(255,255,255,.25);display:flex;align-items:center;justify-content:center}
.tile{position:absolute;border-radius:12px;border:5px solid var(--blue-deep);background:linear-gradient(135deg,#dfe6ee,#8fa3b8)}
.hero-chevron{position:absolute;left:588px;top:628px}

/* welcome */
.welcome-photo{position:absolute;left:0;top:642px;width:625px;height:411px;background:linear-gradient(180deg,#f3f4f6 0%,#d9dde2 60%,#eceef0 100%)}
.section-title{font-family:"Roboto Condensed",sans-serif;font-weight:400;letter-spacing:3px;color:var(--blue);font-size:42px}
.welcome-title{position:absolute;left:602px;top:730px}
.welcome-sub{position:absolute;left:602px;top:798px;font-size:31px;color:#7c7f84;font-weight:400}
.welcome-text{position:absolute;left:602px;top:847px;width:520px;font-size:14px;line-height:23px;color:#4a4f56}
.btn-blue{position:absolute;background:var(--blue);color:var(--white);font-size:20px;display:flex;align-items:center;justify-content:center}

/* services */
.services{position:absolute;top:1058px;left:0;width:1200px;height:700px;background:radial-gradient(ellipse at 50% 45%,var(--blue-light) 0%,var(--blue) 55%,var(--blue-deep) 100%);clip-path:polygon(0 28px,100% 0,100% 662px,50% 700px,0 662px)}
.services-title{position:absolute;left:0;width:1200px;top:1142px;text-align:center;color:var(--white)}
.timeline{position:absolute;left:600px;top:1095px;width:2px;height:658px;background:rgba(255,255,255,.75)}
.node{position:absolute;left:593px;width:16px;height:16px;background:var(--white);border-radius:3px;border:3px solid var(--blue)}
.service-name{position:absolute;font-family:"Roboto Condensed",sans-serif;font-weight:700;font-size:26px;color:var(--white);line-height:31px}
.service-text{position:absolute;font-size:14.5px;line-height:21px;color:#e8f1fa;width:300px}
.right{text-align:right}
.icon-box{position:absolute;width:111px;height:111px;border:2px solid var(--white);border-radius:8px;display:flex;align-items:center;justify-content:center}
.icon-box.featured{background:var(--blue-deep);box-shadow:0 0 24px rgba(255,255,255,.6)}

/* contact */
.contact-bg{position:absolute;top:1720px;left:0;width:1200px;height:440px;background:linear-gradient(180deg,#ffffff 0%,#f1f2f4 70%,#dde1e6 100%)}
.contact-photo{position:absolute;left:774px;top:1794px;width:426px;height:354px;background:linear-gradient(160deg,#c4ccd6 0%,#7f8fa2 55%,#4a5566 100%);border-radius:40px 0 0 0}
.contact-title{position:absolute;left:0;width:1200px;top:1808px;text-align:center}
.contact-intro{position:absolute;left:90px;top:1881px;font-size:13.5px;color:#5c6168}
.field{position:absolute;border-bottom:1px solid var(--line);font-size:13px;color:#9a9ea4;padding-bottom:8px}

/* footer */
.footer{position:absolute;top:2148px;left:0;width:1200px;height:268px;background:linear-gradient(180deg,#1f2a37,#151d27);clip-path:polygon(0 0,50% 22px,100% 0,100% 100%,0 100%)}
.f-icon{position:absolute;width:50px;height:46px;background:var(--white);display:flex;align-items:center;justify-content:center}
.f-text{position:absolute;color:#e4e7eb;font-size:17px}
.f-rule{position:absolute;left:77px;top:2337px;width:1046px;height:1px;background:#3a7fc0}
.f-link{position:absolute;top:2362px;font-size:16px;color:#e4e7eb}
.f-link.active{color:#3a8fd6}
.social{position:absolute;top:2367px;width:15px;height:15px;border-radius:50%;background:var(--white)}
.copyright{position:absolute;top:2416px;left:0;width:1200px;height:53px;background:var(--blue);color:var(--white);font-size:14px;display:flex;align-items:center;justify-content:center;gap:6px}
.copyright strong{font-size:18px;font-weight:700}
</style>
</head>
<body>

<header class="site-nav">
  <span class="nav-link active" style="left:278px">Home</span>
  <span class="nav-link" style="left:415px">About Us</span>
  <div class="brand"><span class="brand-mark"></span>NorvaleData Ltd</div>
  <span class="nav-link" style="left:778px">Services</span>
  <span class="nav-link" style="left:940px">Contact Us</span>
</header>

<section class="hero" role="img" aria-label="Dark city skyline with a business person in the background">
  <h1 class="hero-title">NorvaleData Ltd.</h1>
  <h2 class="hero-sub">We are specialises in data</h2>
  <p class="hero-text">Lorem Ipsum is simply dummy text of the printing and typesetting industry. has been the industry's standard dummy text ever since the.</p>
  <a class="btn-light">READ MORE</a>
  <div class="slider-arrow" style="left:14px"><svg width="20" height="16" viewBox="0 0 20 16"><path d="M9 2 3 8l6 6M17 2l-6 6 6 6" fill="none" stroke="#2b8ad8" stroke-width="2"/></svg></div>
  <div class="slider-arrow" style="left:1134px"><svg width="20" height="16" viewBox="0 0 20 16"><path d="m3 2 6 6-6 6M11 2l6 6-6 6" fill="none" stroke="#2b8ad8" stroke-width="2"/></svg></div>
  <div class="tile" style="left:885px;top:28px;width:185px;height:182px" role="img" aria-label="Business meeting with a digital globe"></div>
  <div class="tile" style="left:700px;top:130px;width:82px;height:82px" role="img" aria-label="Two colleagues at work"></div>
  <div class="tile" style="left:785px;top:214px;width:95px;height:95px" role="img" aria-label="Businessman walking in an office"></div>
  <div class="tile" style="left:1025px;top:244px;width:75px;height:75px" role="img" aria-label="Team portrait"></div>
  <div class="tile" style="left:672px;top:311px;width:115px;height:118px" role="img" aria-label="Team working at a table"></div>
  <div class="tile" style="left:885px;top:315px;width:135px;height:138px" role="img" aria-label="Hand touching a digital interface"></div>
  <div class="tile" style="left:793px;top:459px;width:85px;height:85px" role="img" aria-label="Laptop on a desk"></div>
</section>
<svg class="hero-chevron" width="24" height="24" viewBox="0 0 24 24"><path d="m5 4 7 7 7-7M5 12l7 7 7-7" fill="none" stroke="#fff" stroke-width="2.4"/></svg>

<div class="welcome-photo" role="img" aria-label="Businesswoman typing on a laptop at a white desk"></div>
<h2 class="section-title welcome-title">WELCOME TO NORVALE DATA</h2>
<p class="welcome-sub">We are specialises in data.</p>
<p class="welcome-text">Lorem Ipsum is simply dummy text of the printing and typesetting industry. Lorem Ipsum has been the industry's standard dummy text ever since the 1500s, when an unknown printer took a galley of type and scrambled it to make a type specimen book when an unknown printer took a galley of type and scrambled it to make a type specimen book printer took a galley of type and scrambled.</p>
<a class="btn-blue" style="left:599px;top:981px;width:178px;height:51px">READ MORE</a>

<section class="services" role="img" aria-label="Faint pattern of technology icons on blue"></section>
<h2 class="section-title services-title">OUR SERVICES</h2>
<div class="timeline"></div>
<div class="node" style="top:1096px"></div>
<div class="node" style="top:1310px"></div>
<div class="node" style="top:1438px"></div>
<div class="node" style="top:1521px"></div>
<div class="node" style="top:1644px"></div>

<h3 class="service-name right" style="left:120px;width:300px;top:1275px">Data Governance</h3>
<p class="service-text right" style="left:120px;top:1315px">Lorem Ipsum is simply dummy text of the printing and typesetting.</p>
<div class="icon-box featured" style="left:449px;top:1266px">
  <svg width="64" height="64" viewBox="0 0 64 64" fill="#fff"><ellipse cx="26" cy="14" rx="18" ry="6"/><path d="M8 20c0 3 8 6 18 6s18-3 18-6v8c0 3-8 6-18 6S8 31 8 28z"/><path d="M8 34c0 3 8 6 18 6 3 0 6 0 8-1v9c-2 1-5 1-8 1-10 0-18-3-18-6z"/><circle cx="46" cy="44" r="9" fill="none" stroke="#fff" stroke-width="4"/><circle cx="46" cy="44" r="3"/></svg>
</div>

<div class="icon-box" style="left:632px;top:1391px">
  <svg width="60" height="60" viewBox="0 0 60 60" fill="none" stroke="#fff" stroke-width="2"><rect x="8" y="10" width="44" height="30"/><path d="M14 34l8-10 8 6 10-12M30 40v10M22 52l8-12 8 12"/></svg>
</div>
<h3 class="service-name" style="left:765px;top:1389px;width:320px">Business Intelligence Implemention</h3>
<p class="service-text" style="left:765px;top:1460px">Lorem Ipsum is simply dummy text of the printing and typesetting.</p>

<h3 class="service-name right" style="left:128px;width:300px;top:1488px">Report Modelling</h3>
<p class="service-text right" style="left:128px;top:1527px">Lorem Ipsum is simply dummy text of the printing and typesetting.</p>
<div class="icon-box" style="left:449px;top:1475px">
  <svg width="56" height="60" viewBox="0 0 56 60" fill="none" stroke="#fff" stroke-width="2"><path d="M10 6h26l10 10v38H10z"/><path d="M17 44V34M24 44V26M31 44V30M38 44V22M16 48h24"/></svg>
</div>

<div class="icon-box" style="left:632px;top:1595px">
  <svg width="60" height="60" viewBox="0 0 60 60" fill="none" stroke="#fff" stroke-width="2"><rect x="8" y="8" width="34" height="12"/><rect x="8" y="24" width="34" height="12"/><rect x="8" y="40" width="34" height="12"/><circle cx="44" cy="42" r="10" fill="#0e6db7"/><rect x="39" y="41" width="10" height="7"/><path d="M41 41v-3a3 3 0 0 1 6 0v3"/></svg>
</div>
<h3 class="service-name" style="left:765px;top:1606px">Data Protection</h3>
<p class="service-text" style="left:765px;top:1647px">Lorem Ipsum is simply dummy text of the printing and typesetting.</p>

<div class="contact-bg"></div>
<div class="contact-photo" role="img" aria-label="Hand holding a smartphone showing a contact screen"></div>
<h2 class="section-title contact-title">CONTACT US NOW</h2>
<p class="contact-intro">If you have any questions about how we can help you please either send us an email or call us on below details...</p>
<div class="field" style="left:165px;top:1930px;width:255px">Name</div>
<div class="field" style="left:431px;top:1928px;width:252px">Email Id</div>
<div class="field" style="left:165px;top:1975px;width:518px;height:83px">Message...</div>
<a class="btn-blue" style="left:313px;top:2063px;width:197px;height:51px">SUBMIT</a>

<footer class="footer" role="img" aria-label="Dim office interior with people in the background"></footer>
<div class="f-icon" style="left:128px;top:2237px"><svg width="20" height="24" viewBox="0 0 20 24"><path d="M10 1a8 8 0 0 0-8 8c0 6 8 14 8 14s8-8 8-14a8 8 0 0 0-8-8z" fill="#1f2a37"/><circle cx="10" cy="9" r="3" fill="#fff"/></svg></div>
<p class="f-text" style="left:197px;top:2236px;width:200px;font-size:13px;line-height:22px">Lorem Ipsum is simply dummy text of the printing &amp; typesetting industry.</p>
<div class="f-icon" style="left:502px;top:2237px"><svg width="22" height="22" viewBox="0 0 24 24"><path d="M6 2h4l2 5-3 2a12 12 0 0 0 6 6l2-3 5 2v4a2 2 0 0 1-2 2A18 18 0 0 1 4 4a2 2 0 0 1 2-2z" fill="#1f2a37"/></svg></div>
<p class="f-text" style="left:571px;top:2248px">020 7946 0321</p>
<div class="f-icon" style="left:816px;top:2237px"><svg width="22" height="18" viewBox="0 0 22 18"><rect x="1" y="2" width="20" height="14" fill="#1f2a37"/><path d="m1 3 10 7 10-7" fill="none" stroke="#fff" stroke-width="1.6"/></svg></div>
<p class="f-text" style="left:885px;top:2248px">info@norvaledata.co.uk</p>
<div class="f-rule"></div>
<span class="f-link active" style="left:80px">Home</span>
<span class="f-link" style="left:160px">About Us</span>
<span class="f-link" style="left:267px">Services</span>
<span class="f-link" style="left:362px">Contact Us</span>
<span class="social" style="left:952px"></span>
<span class="social" style="left:989px"></span>
<span class="social" style="left:1028px"></span>
<span class="social" style="left:1068px"></span>
<span class="social" style="left:1107px"></span>
<div class="copyright">© <strong>NorvaleData Ltd.</strong> - 2017. All rights reserved.</div>

</body>
</html>
```